domestic violence campaign

To Whom It May Concern:

We are fully aware that domestic violence can enter anyone’s life at any given time. As women we are faced with many demands as mothers, daughters, wives, sisters, providers, and friends. We often lose ourselves and our confidence. Bright Maple Circle (BMC) Transitional Center of Western New York has embarked on a whole new way of intervention and prevention. As a domestic violence survivor I have created a facility and ideals which will enforce a revolution of Domestic Violence victims. For many years, growing up in suburbs of Western New York, I have come to terms with this fight. Domestic Violence can be stopped and prevented. As a domestic violence victim myself, being in live-in facility, as well as six different domestic violence shelters throughout the state, I fled from my domestic violence abuse. Without those temporary facilities, all that comes to my mind is death. They helped me rebuild and save my life but something was missing – zero education, training programs, parenting classes, personal strengthening workshops, on site at all. Considering the limited amount of time (30-45 days in an average shelter) and lack of resources, I was in need of the tools needed to move me from being a victim to having a stable life.
Opening more doors in Western New York is essential with the surrounding agencies and shelters overwhelmed from assisting women of crisis. Many issues have risen, as a result, such as: over-crowding, long waiting lists, and zero educational training with an on-site teaching curriculum. A repeated vicious cycle – victims regressing and not progressing with over 4000 cases of domestic violence reported throughout Erie County. The opening Bright Maple Circle (BMC) Transitional Center of Western New York will provide a 9-24 month live-in facility, along with educational and training programs on-site that will serve as important tools to domestic violence victims. These educational based facilities and services are well needed for Western New York. Our trained certified staff will provide endless help to domestic violence victim. They will feel safe as they rebuild their lives and take advantage of our educational curriculum that has been designed to increase awareness and provide steppingstones to move the victims into confident stable independent human beings. Our clients will receive complete educational training, state testing, parenting classes, as well as strengthening, coping, and developing skills here at our facility. Bright Maple Circle (BMC) Transitional Center is asking for your support.
Sincerely,
Rosalind Pemberton
President and CEO/website bmctcq.org
Bright Maple Circle (BMC) Transitional Center of WNY

Industry/Entity Type

Training

Requirements
Nice to have
• we have already created our T-shirt/we will like for our T-shirt to be the center of the campaign to T-shirt reads
V IOLENCE
O N
W OMEN
S TOPS the campaign is to raise money so we can open doors and save lives

```html
<!DOCTYPE html>
<html lang="en">
<head>
<meta charset="utf-8">
<title>Bright Maple Circle – Domestic Violence Campaign</title>
<link rel="stylesheet" href="https://fonts.googleapis.com/css2?family=Roboto+Condensed:wght@300;400;700&family=Roboto:wght@300;400&display=swap">
<style>
  :root {
    --purple: #5a2a7f;
    --purple-bright: #7b2f93;
    --ink: #3a3a3c;
    --panel-edge: #dcdcdd;
    --panel-mid: #f7f7f7;
    --page: #ffffff;
  }
  * { margin: 0; padding: 0; box-sizing: border-box; }
  html, body {
    width: 1200px; height: 923px; overflow: hidden;
    background: var(--page);
  }
  .ad {
    position: absolute; left: 30px; top: 30px;
    width: 1138px; height: 863px;
    background: radial-gradient(ellipse 55% 60% at 50% 45%, var(--panel-mid) 0%, #ededee 60%, var(--panel-edge) 100%);
    color: var(--ink);
    font-family: "Roboto Condensed", "Arial Narrow", sans-serif;
  }
  .brand { position: absolute; left: 22px; top: 34px; display: flex; align-items: center; gap: 18px; }
  .brand-dot { width: 104px; height: 82px; }
  .brand-text { line-height: 1; }
  .brand-name { font-family: "Roboto Condensed", sans-serif; font-weight: 700; font-size: 29px; color: var(--purple-bright); }
  .brand-sub { font-family: "Roboto", sans-serif; font-weight: 400; font-size: 25px; color: var(--ink); margin-top: 4px; }
  .brand-region { font-family: "Roboto", sans-serif; font-size: 13px; letter-spacing: .3px; color: var(--ink); margin-top: 4px; padding-left: 85px; }

  .donate { position: absolute; right: 30px; top: 30px; text-align: right; }
  .donate-call { font-weight: 700; font-size: 62px; line-height: .84; color: var(--purple); }
  .donate-url { font-family: "Roboto", sans-serif; font-size: 23px; margin-top: 14px; color: var(--ink); letter-spacing: .5px; }

  .message { position: absolute; left: 98px; top: 226px; width: 520px; }
  .line { display: block; font-size: 56px; line-height: 60px; font-weight: 300; white-space: nowrap; }
  .line strong { font-weight: 700; color: var(--purple); }
  .line.lead { font-weight: 700; color: var(--purple); letter-spacing: 2px; font-size: 54px; }
  .line.wide { letter-spacing: 2.4px; font-family: "Roboto", sans-serif; font-size: 48px; }
  .line.tight { letter-spacing: -1px; font-family: "Roboto", sans-serif; font-size: 48px; }
  .block + .block { margin-top: 54px; }

  .pledge { position: absolute; left: 98px; top: 705px; font-family: "Roboto", sans-serif; font-size: 27px; line-height: 36px; letter-spacing: -.3px; }
  .pledge .indent { padding-left: 40px; }
  .pledge em { font-style: normal; color: var(--purple-bright); font-family: "Roboto Condensed", sans-serif; font-size: 30px; }

  .portrait {
    position: absolute; left: 700px; top: 238px; width: 430px; height: 532px;
    border-radius: 180px 180px 0 0;
    background: linear-gradient(180deg, #6b4536 0%, #8a5d47 40%, #e9a81c 62%, #f3bd2a 100%);
  }

  .tagline { position: absolute; right: 24px; bottom: 20px; font-family: "Roboto", sans-serif; font-size: 25px; letter-spacing: 1.5px; }
  .tagline strong { font-family: "Roboto Condensed", sans-serif; font-weight: 700; color: var(--purple); letter-spacing: 0; }
</style>
</head>
<body>
  <main class="ad">
    <header class="brand">
      <svg class="brand-dot" viewBox="0 0 104 82" aria-hidden="true"><circle cx="52" cy="41" r="38" fill="var(--purple)"/></svg>
      <div class="brand-text">
        <div class="brand-name">Bright Maple Circle</div>
        <div class="brand-sub">Transitional Center</div>
        <div class="brand-region">WESTERN NEW YORK</div>
      </div>
    </header>

    <aside class="donate">
      <div class="donate-call">DONATE<br>TODAY!</div>
      <div class="donate-url">BMCTCQ.ORG</div>
    </aside>

    <section class="message">
      <p class="block">
        <span class="line lead">DOMESTIC VIOLENCE</span>
        <span class="line wide">CAN ENTER ANYONE’S</span>
        <span class="line tight">LIFE AT ANY GIVEN <strong>TIME.</strong></span>
      </p>
      <p class="block">
        <span class="line wide">DOMESTIC VIOLENCE</span>
        <span class="line wide">CAN BE <strong>STOPPED</strong> OR</span>
        <span class="line"><strong>PREVENTED.</strong></span>
      </p>
    </section>

    <p class="pledge">PLACE YOUR AD, AND SPEAK OUT:<br><span class="indent">TAKE THE “<em>VOWS WITH BMC</em>.”</span></p>

    <div class="portrait" role="img" aria-label="Photo of a smiling woman with brown hair wearing a yellow T-shirt, arms crossed"></div>

    <footer class="tagline">VIOLENCE ON WOMEN <strong>STOP NOW.</strong></footer>
  </main>
</body>
</html>
```